Thank You Card

I'm looking for a thank you card design using our logo and other graphics. We are an essential business and our employees (Electricians) have done an incredible job staying healthy and safe during the COVID-19 pandemic, I want to send each a thank you card.

```html
<!DOCTYPE html>
<html lang="en">
<head>
<meta charset="utf-8">
<title>Thank You Card</title>
<link href="https://fonts.googleapis.com/css2?family=Arimo:wght@400;700&family=Yellowtail&display=swap" rel="stylesheet">
<style>
  :root {
    --card-red: #e8283a;
    --card-blue: #5361b3;
    --card-white: #ffffff;
    --ink-grey: #4a4a4a;
    --line-grey: #555555;
    --page-bg: #ebe9e5;
  }
  html, body {
    margin: 0;
    padding: 0;
    width: 1200px;
    height: 900px;
    overflow: hidden;
    background: var(--page-bg);
  }
  .canvas {
    position: relative;
    width: 1200px;
    height: 900px;
  }
  .card {
    position: absolute;
    width: 570px;
    height: 379px;
    background: var(--card-white);
    box-shadow: 0 2px 6px rgba(0,0,0,0.18);
  }
  .card svg { display: block; width: 100%; height: 100%; }
  .card--back { left: 60px; top: 50px; }
  .card--front { left: 570px; top: 470px; }

  .sans { font-family: "Arimo", Arial, sans-serif; }
  .script { font-family: "Yellowtail", cursive; }

  .brand-name { font-family: "Arimo", Arial, sans-serif; font-weight: 700; fill: var(--card-red); }
  .contact-line { font-family: "Arimo", Arial, sans-serif; font-size: 11.5px; fill: var(--ink-grey); }
  .postal-line { stroke: var(--line-grey); stroke-width: 1.3; fill: none; }

  .greeting { font-family: "Yellowtail", cursive; font-size: 150px; }
  .greeting--shade { fill: var(--card-blue); }
  .greeting--face { fill: var(--card-red); }
  .message { font-family: "Arimo", Arial, sans-serif; font-size: 27px; fill: var(--card-white); }
  .message strong, .message .bold { font-weight: 700; }
  .brand-name--light { font-family: "Arimo", Arial, sans-serif; font-weight: 700; font-size: 15px; fill: var(--card-white); }
</style>
</head>
<body>
<main class="canvas">

  <!-- Address side -->
  <section class="card card--back" aria-label="Card address side">
    <svg viewBox="0 0 692 460" xmlns="http://www.w3.org/2000/svg">
      <text class="brand-name" x="175" y="212" font-size="42" text-anchor="middle">BRIGHTLINE</text>
      <text class="brand-name" x="175" y="252" font-size="28" text-anchor="middle">ELECTRIC INC.</text>

      <g class="dot-row" fill="var(--card-red)">
        <circle cx="135" cy="362" r="3.2"/>
        <circle cx="151" cy="362" r="3.2"/>
        <circle cx="167" cy="362" r="3.2"/>
        <circle cx="183" cy="362" r="3.2"/>
        <circle cx="199" cy="362" r="3.2"/>
      </g>

      <g class="contact-block">
        <!-- phone icon -->
        <path d="M85 383 q0 -2 2 -2 l2 0 l1 3 l-1.5 1 q1 2.5 3 3.5 l1 -1.5 l3 1 l0 2 q0 2 -2 2 q-8 -1 -8.5 -9 z" fill="var(--card-red)"/>
        <text class="contact-line" x="97" y="392">555-014-2871</text>
        <!-- mobile icon -->
        <rect x="176" y="382" width="6" height="10" rx="1" fill="none" stroke="var(--card-red)" stroke-width="1.4"/>
        <text class="contact-line" x="186" y="392">555-014-3392</text>

        <!-- fax icon -->
        <rect x="48" y="402" width="10" height="6" rx="1" fill="var(--card-red)"/>
        <rect x="50" y="399" width="6" height="3" fill="var(--card-red)"/>
        <text class="contact-line" x="61" y="408">555-014-7710</text>
        <!-- mail icon -->
        <rect x="143" y="401" width="9" height="6.5" fill="var(--card-red)"/>
        <path d="M143 401 l4.5 3.5 l4.5 -3.5" stroke="var(--card-white)" stroke-width="0.9" fill="none"/>
        <text class="contact-line" x="155" y="408">hello@BrightlineElectric</text>

        <text class="contact-line" x="175" y="423" text-anchor="middle">www.BrightlineElectric.com</text>
      </g>

      <line class="postal-line" x1="357" y1="60" x2="357" y2="300"/>
      <rect class="postal-line" x="565" y="55" width="80" height="78"/>
      <line class="postal-line" x1="384" y1="268" x2="652" y2="268"/>
    </svg>
  </section>

  <!-- Greeting side -->
  <section class="card card--front" aria-label="Card greeting side">
    <svg viewBox="0 0 692 460" xmlns="http://www.w3.org/2000/svg">
      <!-- top band -->
      <path class="band-stripe" d="M0 0 H692 V6 C560 66 430 88 310 86 C180 82 80 40 0 0 Z" fill="var(--card-blue)"/>
      <path class="band-fill" d="M44 0 H692 V2 C560 58 430 80 310 78 C190 74 110 36 44 0 Z" fill="var(--card-red)"/>

      <!-- bottom band -->
      <path class="band-stripe" d="M0 332 C130 278 260 254 385 256 C505 260 600 298 692 340 V460 H0 Z" fill="var(--card-blue)"/>
      <path class="band-fill" d="M0 344 C130 288 260 264 385 266 C505 270 600 308 692 356 V460 H0 Z" fill="var(--card-red)"/>

      <!-- greeting -->
      <text class="greeting greeting--shade" x="343" y="213" text-anchor="middle">Thank you</text>
      <text class="greeting greeting--face" x="346" y="210" text-anchor="middle">Thank you</text>

      <text class="message" x="346" y="340" text-anchor="middle">for staying healthy &amp; safe during</text>
      <text class="message" x="346" y="376" text-anchor="middle">the <tspan class="bold" font-weight="700">COVID-19</tspan> pandemic</text>

      <text class="brand-name--light" x="335" y="418" text-anchor="middle">BRIGHTLINE ELECTRIC INC.</text>
    </svg>
  </section>

</main>
</body>
</html>
```